We need letterhead, Business Cards, and envelops designed. We have attached a design of our logo and a sample of letterhead idea that was started but never perfected, it is only an idea for the letterhead if you can design something better we may love that also we are open to change.
We want a design that looks professional in style. we are a non profit trade association in the construction industry. the green color in the attached design represent green building, and we like that. also if you just want to enhance the letterhead sample that we attached that would be fine also.
Thanks and good luck
also the name that should show on the first business cards should be Merwin Habsfield, Director are web address is www.tqvmp.org

```html
<!DOCTYPE html>
<html lang="en">
<head>
<meta charset="utf-8">
<title>Verdant Builders Alliance — Letterhead</title>
<link href="https://fonts.googleapis.com/css2?family=Arimo:wght@400;700&family=Raleway:wght@300;400&display=swap" rel="stylesheet">
<style>
  :root {
    --backdrop: #e4e5e6;
    --paper: #ffffff;
    --ink: #1a1a1a;
    --band: #0d0d0d;
    --band-text: #d9d9d9;
    --green: #6f9a3c;
    --green-soft: #dfe8d2;
    --green-faint: #eef3e7;
  }
  * { box-sizing: border-box; margin: 0; padding: 0; }
  html, body {
    width: 1200px; height: 909px; overflow: hidden;
    background: var(--backdrop);
  }
  .letterhead {
    position: absolute; left: 264px; top: 20px;
    width: 672px; height: 869px;
    background: var(--paper);
    box-shadow: 0 4px 18px rgba(0,0,0,0.18);
    font-family: "Arimo", Arial, sans-serif;
    color: var(--ink);
    overflow: hidden;
  }
  .brand {
    position: absolute; top: 58px; left: 0; width: 100%;
    display: flex; justify-content: center; align-items: center; gap: 10px;
  }
  .brand-mark { width: 14px; height: 14px; background: var(--green); }
  .brand-name {
    font-size: 22px; font-weight: 700; letter-spacing: 0.5px; color: var(--ink);
  }
  .letter {
    position: absolute; top: 150px; left: 70px; width: 520px;
    font-size: 10.5px; line-height: 1.42;
  }
  .letter-head p { margin: 0; }
  .salutation { margin: 18px 0 12px; }
  .letter-body p { margin-bottom: 12px; }
  .closing { margin-top: 22px; }
  .signature { margin-top: 34px; }
  .building-art {
    position: absolute; right: 60px; top: 520px;
    width: 260px; height: 200px;
    background: linear-gradient(180deg, var(--green-faint), var(--green-soft));
    opacity: 0.7;
  }
  .footer-band {
    position: absolute; left: 0; bottom: 0; width: 100%; height: 150px;
    background: var(--band);
    font-family: "Raleway", Arial, sans-serif; font-weight: 300;
    color: var(--band-text); font-size: 11px; letter-spacing: 1.6px;
    line-height: 1.55;
  }
  .footer-address { position: absolute; left: 70px; bottom: 36px; }
  .footer-contact {
    position: absolute; right: 70px; top: 26px;
    display: grid; grid-template-columns: 12px auto; column-gap: 12px; align-items: center;
  }
  .footer-contact svg { width: 10px; height: 10px; fill: var(--green); }
</style>
</head>
<body>
  <main class="letterhead">
    <header class="brand">
      <span class="brand-mark"></span>
      <span class="brand-name">Verdant Builders Alliance</span>
    </header>

    <article class="letter">
      <div class="letter-head">
        <p>June 26, 2014</p>
        <p>Trenz Pruca</p>
        <p>Title</p>
        <p>Company Name</p>
        <p>4321 First Street</p>
        <p>Anytown, State ZIP</p>
      </div>
      <p class="salutation">Dear Trenz,</p>
      <div class="letter-body">
        <p>Lorem ipsum dolor sit amet, consectetur adipiscing elit, sed eiusmod tempor incidunt et labore et dolore magna aliquam. Ut enim ad minim veniam, quis nostrud exerc. Irure dolor in reprehend incididunt ut labore et dolore magna aliqua. Ut enim ad minim veniam, quis nostrud exercitation ullamco laboris nisi ut aliquip ex ea commodo consequat. Duis aute irure dolor in reprehenderit in voluptate velit esse molestaie cillum. Tia non ob ea soluad incom dereud facilis est er expedit distinct.</p>
        <p>At vver eos et accusam dignissum qui blandit est praesent. Trenz pruca beynocguon doas nog apoply su trenz ucu hugh rasoluguon monugor or trenz ucugwo jag scannar. Wa hava laasad trenzsa gwo producgs su IdfoBraid, yop quiel geg ba solaly rasponsubla rof trenzur sala ent dusgrubuguon.</p>
        <p>Plloaso mako nuto uf cakso dodtos anr koop a cupy uf cak vux noaw yerw phuno. Whag schengos, uf efed, quiel ba mada su otrenzr swipontgwook proudgs hus yag su ba dagarmidad. Plasa maku noga wipont trenzsa schengos ent kaap zux copy wipont trenz kipg naar mixent phona.</p>
        <p>Lorem ipsum dolor sit amet, consectetur adipiscing elit. Donec id erat quis metus suscipit mattis. Duis elit velit, venenatis id ullamcorper at, sollicitudin nec eros. Vivamus ultricies dapibus neque et laoreet condimentum convallis quis a lacus.</p>
      </div>
      <p class="closing">Sincerely yours,</p>
      <p class="signature">Urna Semper</p>
    </article>

    <div class="building-art" role="img" aria-label="Faint green building outline decoration"></div>

    <footer class="footer-band">
      <address class="footer-address" style="font-style:normal">
        address<br>4321 first street<br>anytown, State ZIP
      </address>
      <div class="footer-contact">
        <svg viewBox="0 0 10 10" aria-hidden="true"><path d="M2 0h2l1 3-1.5 1a6 6 0 0 0 2.5 2.5L7 5l3 1v2a2 2 0 0 1-2 2A8 8 0 0 1 0 2a2 2 0 0 1 2-2z"/></svg>
        <span>123-456-7890</span>
        <svg viewBox="0 0 10 10" aria-hidden="true"><rect x="1" y="3" width="8" height="6"/><rect x="3" y="0" width="4" height="3"/></svg>
        <span>123-456-7891</span>
        <svg viewBox="0 0 10 10" aria-hidden="true"><circle cx="5" cy="5" r="5"/></svg>
        <span>www.tqvmp.org</span>
      </div>
    </footer>
  </main>
</body>
</html>
```